Brackenfield Vale Country Club Business Sponsorship Package

Need a flyer to promote new business sponsorship packageCost 4500 + GST12 months sponsorship and promotion via BVCC Corporate Partners listing $1000 Food & Beverage House AccountMembers Welcome PackChristmas Party Invite7 Day with Cart Golf Membership10% discount on events and showsPayable over 4 installments

Target Market(s)

Business Owners who play Golf

Industry/Entity Type

Golf Course

```html
<!DOCTYPE html>
<html lang="en">
<head>
<meta charset="utf-8">
<title>Brackenfield Vale Country Club – Sponsorship Package</title>
<link rel="stylesheet" href="https://fonts.googleapis.com/css2?family=Bebas+Neue&family=Titan+One&family=Patrick+Hand&family=Cinzel:wght@600&display=swap">
<style>
  :root{
    --paper:#ffffff;
    --board:#1c1c1c;
    --board-light:#2b2b2b;
    --chalk:#f2f2f2;
    --chalk-line:#8c8c8c;
    --orange:#e07a2c;
    --red:#ee1c24;
    --smudge:#5a5a5a;
    --dash:#6a6a6a;
    --silhouette:#e2e2e2;
    --ink:#1a1a1a;
  }
  *{margin:0;padding:0;box-sizing:border-box}
  html,body{width:903px;height:1200px;overflow:hidden;background:#d9d9d9}
  .flyer{position:relative;width:903px;height:1200px;overflow:hidden;background:radial-gradient(ellipse at 50% 55%,var(--board-light),var(--board) 75%)}
  .header{position:absolute;left:0;top:0;width:903px;height:230px;background:var(--paper)}
  .club-name{position:absolute;top:52px;left:0;width:903px;text-align:center;font-family:"Cinzel",serif;font-weight:600;font-size:26px;color:var(--ink);letter-spacing:0.5px}
  .club-name .mark{display:inline-block;width:14px;height:14px;border:2px solid var(--ink);margin-right:12px;vertical-align:2px}
  .scene-strip{position:absolute;left:170px;top:110px;width:560px;height:100px;background:radial-gradient(ellipse at 50% 90%,var(--silhouette),rgba(255,255,255,0) 70%)}
  .torn-edge{position:absolute;left:0;top:196px;width:903px;height:40px}
  .title{position:absolute;top:252px;left:0;width:903px;text-align:center;font-family:"Bebas Neue",sans-serif;font-size:92px;color:var(--chalk);letter-spacing:1px;line-height:1}
  .price{position:absolute;top:326px;left:100px;display:flex;align-items:flex-start;font-family:"Titan One",sans-serif;color:var(--red);line-height:1}
  .price .currency{font-size:96px;margin-top:22px;margin-right:-4px}
  .price .amount{font-size:190px;letter-spacing:-5px}
  .gst{position:absolute;top:392px;left:664px;font-family:"Bebas Neue",sans-serif;font-size:72px;color:var(--orange);line-height:1}
  .features-heading{position:absolute;top:566px;left:0;width:903px;text-align:center;font-family:"Bebas Neue",sans-serif;font-size:46px;line-height:1}
  .features-heading span{display:inline-block;padding:4px 16px 0;background:linear-gradient(90deg,transparent,var(--smudge) 8%,var(--smudge) 92%,transparent);color:var(--chalk)}
  .features-heading em{font-style:normal;color:var(--orange)}
  .overlay{position:absolute;left:0;top:0}
  .icon{fill:none;stroke:var(--chalk-line);stroke-width:2.5;stroke-linecap:round;stroke-linejoin:round}
  .chalk-art{position:absolute;border-radius:50%;background:radial-gradient(circle,rgba(200,200,200,.16),rgba(200,200,200,0) 70%)}
  .feature{position:absolute;font-family:"Patrick Hand",cursive;color:var(--chalk);line-height:1.15}
  .feature .hl{color:var(--orange)}
  .f-partners{left:200px;top:664px;width:320px;text-align:center;font-size:23px;line-height:27px}
  .f-welcome{left:620px;top:694px;width:260px;text-align:center;font-size:30px}
  .f-discount{left:188px;top:856px;font-size:32px}
  .f-xmas{left:606px;top:852px;width:260px;text-align:center;font-size:31px}
  .f-golf{left:238px;top:1002px;font-size:31px}
  .f-payable{left:638px;top:1013px;font-size:29px}
  .footer{position:absolute;top:1144px;left:0;width:903px;text-align:center;font-family:"Patrick Hand",cursive;line-height:1}
  .footer .strip{display:inline-block;padding:6px 30px;background:linear-gradient(90deg,transparent,var(--smudge) 6%,var(--smudge) 94%,transparent)}
  .footer .lead{font-size:21px;color:var(--orange);margin-right:6px}
  .footer .url{font-size:27px;color:var(--chalk)}
</style>
</head>
<body>
<main class="flyer">
  <header class="header">
    <div class="club-name"><span class="mark"></span>BRACKENFIELD VALE COUNTRY CLUB</div>
    <div class="scene-strip" role="img" aria-label="Faint silhouettes of golfers, dancers, a wedding couple and diners"></div>
  </header>
  <svg class="torn-edge" viewBox="0 0 903 40" preserveAspectRatio="none" aria-hidden="true">
    <path d="M0 14 L40 10 L80 17 L120 8 L170 15 L210 9 L260 16 L300 7 L350 14 L400 10 L440 18 L490 8 L540 15 L590 9 L640 16 L690 10 L740 17 L790 8 L840 14 L903 10 L903 40 L0 40Z" fill="#1c1c1c"/>
  </svg>

  <h1 class="title">SPONSORSHIP PACKAGE</h1>
  <div class="price"><span class="currency">$</span><span class="amount">4500</span></div>
  <div class="gst">+ GST</div>

  <h2 class="features-heading"><span>FEATURES <em>INCLUDED</em></span></h2>

  <svg class="overlay" width="903" height="1200" aria-hidden="true">
    <g fill="none" stroke="var(--dash)" stroke-width="1.5" stroke-dasharray="5 5">
      <path d="M240 640 C150 640 60 690 65 760 C70 800 160 800 300 800 C420 800 520 790 520 720 C520 660 470 640 380 632"/>
      <path d="M540 660 C580 640 720 630 800 650 C880 670 890 770 820 790 C740 810 600 800 555 760"/>
      <path d="M80 830 C60 870 80 950 150 955 C300 965 470 960 470 900 C470 850 500 820 600 815 C700 810 820 820 840 860"/>
      <path d="M500 900 C500 950 560 975 650 975 C760 975 840 960 850 920"/>
      <path d="M120 975 C90 1010 100 1100 200 1100 C320 1100 460 1095 480 1050 C500 1000 520 985 600 985 C720 985 860 990 860 1060 C860 1110 780 1120 700 1110"/>
    </g>

    <!-- network -->
    <g class="icon">
      <circle cx="849" cy="377" r="13"/>
      <path d="M843 377 l4 5 l8 -9"/>
      <circle cx="849" cy="349" r="6"/><circle cx="874" cy="362" r="6"/><circle cx="874" cy="393" r="6"/>
      <circle cx="849" cy="405" r="6"/><circle cx="824" cy="393" r="6"/><circle cx="824" cy="362" r="6"/>
      <path d="M849 355 v9 M869 365 l-8 5 M869 390 l-8 -5 M849 399 v-9 M829 390 l8 -5 M829 365 l8 5"/>
    </g>
    <!-- browser window with plus -->
    <g class="icon" transform="rotate(-12 84 493)">
      <rect x="55" y="468" width="58" height="50" rx="3"/>
      <path d="M55 480 h58 M62 474 h2 M68 474 h2"/>
      <path d="M84 489 v20 M74 499 h20"/>
    </g>
    <!-- alarm clock -->
    <g class="icon">
      <circle cx="170" cy="560" r="30"/>
      <path d="M170 560 v-17 M170 560 l13 8"/>
      <path d="M138 540 a14 14 0 0 1 18 -16 M202 540 a14 14 0 0 0 -18 -16"/>
      <path d="M150 586 l-8 10 M190 586 l8 10"/>
    </g>
    <!-- gift -->
    <g class="icon" transform="rotate(10 780 555)">
      <rect x="735" y="545" width="90" height="55"/>
      <rect x="728" y="526" width="104" height="20"/>
      <path d="M780 526 v74"/>
      <path d="M780 526 c-20 -30 -42 -10 -22 0 M780 526 c20 -30 42 -10 22 0"/>
      <path d="M742 560 l25 25 M742 575 l15 15 M795 560 l25 25 M795 575 l15 15"/>
    </g>
    <!-- dollar badge -->
    <g class="icon">
      <path d="M128 836 l6 8 l10 -2 l0 10 l9 5 l-6 8 l6 8 l-9 5 l0 10 l-10 -2 l-6 8 l-6 -8 l-10 2 l0 -10 l-9 -5 l6 -8 l-6 -8 l9 -5 l0 -10 l10 2 z"/>
      <path d="M134 856 c-3 -4 -13 -4 -13 2 c0 6 13 4 13 10 c0 6 -10 6 -13 2 M128 850 v26"/>
    </g>
    <!-- thumbs up -->
    <g class="icon">
      <rect x="102" y="910" width="12" height="30" rx="2"/>
      <path d="M114 912 l12 -14 c3 -6 10 -4 9 3 l-3 10 h16 c5 0 7 4 6 8 l-4 15 c-1 4 -4 6 -8 6 h-28"/>
    </g>
    <!-- golf flag and hole -->
    <g class="icon">
      <ellipse cx="160" cy="1058" rx="48" ry="14"/>
      <ellipse cx="150" cy="1056" rx="7" ry="3"/>
      <path d="M150 1056 v-70"/>
      <path d="M150 986 l28 9 l-28 10"/>
    </g>
    <!-- card payment -->
    <g class="icon" transform="rotate(-10 566 1044)">
      <rect x="528" y="1022" width="78" height="46" rx="5"/>
      <path d="M528 1034 h78 M538 1054 h20"/>
    </g>
  </svg>

  <div class="chalk-art" style="left:68px;top:670px;width:130px;height:110px" role="img" aria-label="Chalk sketch of a businessman with a dollar coin"></div>
  <p class="feature f-partners">12 months sponsorship and promotion via <span class="hl">BVCC Corporate Partners listing $1000 Food &amp; Beverage House Account</span></p>

  <div class="chalk-art" style="left:556px;top:694px;width:90px;height:86px" role="img" aria-label="Chalk sketch of a smiling badge"></div>
  <p class="feature f-welcome">Members<br><span class="hl">Welcome Pack</span></p>

  <p class="feature f-discount">10% discount on<br><span class="hl">events and shows</span></p>

  <div class="chalk-art" style="left:526px;top:842px;width:112px;height:112px" role="img" aria-label="Chalk sketch of Santa for the Christmas party"></div>
  <p class="feature f-xmas">Christmas<br><span class="hl">Party Invite</span></p>

  <p class="feature f-golf">7 Day with Cart<br><span class="hl">Golf Membership</span></p>

  <p class="feature f-payable">Payable over<br><span class="hl">4 installments</span></p>

  <footer class="footer"><span class="strip"><span class="lead">For More information visit,</span><span class="url">www.brackenfieldvale.net.au</span></span></footer>
</main>
</body>
</html>
```